"Tidewell Fellowship" needs a logo design that represents a Christian family boating ministry

Mission Statement:
“Providing compassion, care and opportunities to create memories for marginalized groups of society through ocean therapy.”
Bible verse:
Colossians 3:12 – “Therefore, as God’s chosen people, holy and dearly loved, clothe yourselves with compassion, kindness, humility, gentleness and patience.”
Target Market(s)
HOMELESS (who have gone through shelters and are on the road to recovery)
CHURCH GROUPS
INJURED MILITARY VETERANS
YOUTH AT RISK (orphans, human trafficking survivors)
SICKLY (hospitalized who can get out once in a while)
CAREGIVERS (single moms, military spouses caring for injured vets, families of those in prison)
ELDERLY (retirement centers)
SMALL BUSINESS STAFF OUTINGS
SPECIAL EVENTS
Industry/Entity Type
Ministry
Contact Information for Business Card
Captain Glen Marlowe @ 808-491-3027
Priscilla Marlowe @ 808-493-5184
info@tidewellfellowship.example
www.tidewellfellowship.example (not active yet but hopefully, soon)
Requirements
Must have
- Catch-phrase words maybe for back of business card:
- "Tide-Bound --- Kindness --- Making moments out at sea"
Nice to have
- Added 2 photo files just for visuals:
- 1 photo is of our boat.
- Other photo is our daughter's artwork on a cooler she made (for father's day gift)...might be nice and fun to incorporate daughter's artwork/inspiration into logo...but not sure if it looks to busy

```html
<!DOCTYPE html>
<html lang="en">
<head>
<meta charset="utf-8">
<title>Tidewell Fellowship – Business Cards</title>
<link href="https://fonts.googleapis.com/css2?family=Montserrat:wght@400;500;600&display=swap" rel="stylesheet">
<style>
  :root {
    --stage: #1d1d1f;
    --card-dark: #5b5b5d;
    --card-light: #ffffff;
    --teal: #3a8f9b;
    --ink: #4a4a4c;
    --muted: #6d6d70;
    --white: #ffffff;
  }
  * { box-sizing: border-box; margin: 0; padding: 0; }
  html, body {
    width: 1200px; height: 900px; overflow: hidden;
    background: var(--stage);
    font-family: "Montserrat", Arial, sans-serif;
  }
  .stage {
    width: 1200px; height: 900px;
    display: flex; flex-direction: column;
    align-items: center; justify-content: center; gap: 40px;
  }
  .card {
    width: 620px; height: 354px;
    border-radius: 22px;
    position: relative;
    box-shadow: 0 18px 40px rgba(0,0,0,.45);
  }
  .card-back {
    background: var(--card-dark);
    display: flex; flex-direction: column;
    align-items: center; justify-content: center;
    color: var(--white);
  }
  .wordmark {
    font-weight: 600;
    letter-spacing: .5px;
    line-height: 1.1;
    text-align: center;
  }
  .card-back .wordmark { font-size: 44px; color: var(--white); }
  .tagline {
    margin-top: 56px;
    text-align: center;
    font-size: 13px;
    letter-spacing: .4px;
    line-height: 1.45;
  }
  .tagline .values { text-transform: uppercase; font-weight: 500; }
  .card-front {
    background: var(--card-light);
    display: flex; align-items: center;
    padding: 0 44px 0 40px;
  }
  .card-front .wordmark {
    width: 250px;
    font-size: 32px;
    color: var(--teal);
  }
  .divider {
    width: 1px; height: 150px;
    background: var(--teal);
    margin: 0 34px 0 24px;
  }
  .contact { color: var(--muted); font-size: 13px; line-height: 1.55; }
  .person-name {
    color: var(--teal); font-size: 21px; font-weight: 500;
    text-transform: uppercase; letter-spacing: .3px; line-height: 1.1;
  }
  .person-role { text-transform: uppercase; font-size: 12px; margin-bottom: 8px; }
  .address { margin-bottom: 6px; }
  .contact-line { display: flex; align-items: center; gap: 8px; }
  .contact-line svg { width: 12px; height: 12px; flex: none; }
</style>
</head>
<body>
<main class="stage">
  <section class="card card-back">
    <div class="wordmark">Tidewell<br>Fellowship</div>
    <p class="tagline">
      <span class="values">Tide-Bound - Kindness</span><br>
      Making moments out at sea
    </p>
  </section>

  <section class="card card-front">
    <div class="wordmark">Tidewell<br>Fellowship</div>
    <div class="divider"></div>
    <div class="contact">
      <div class="person-name">Dale Whitcomb</div>
      <div class="person-role">Director</div>
      <div class="address">4820 Harbor Ln 12,<br>Cedar Point County, AB, T0X 1A0</div>
      <div class="contact-line">
        <svg viewBox="0 0 24 24" fill="none" stroke="currentColor" stroke-width="2.2"><path d="M5 3h4l2 5-2.5 1.5a11 11 0 0 0 6 6L16 13l5 2v4a2 2 0 0 1-2 2A17 17 0 0 1 3 5a2 2 0 0 1 2-2z"/></svg>
        (403) 555-0142
      </div>
      <div class="contact-line">
        <svg viewBox="0 0 24 24" fill="none" stroke="currentColor" stroke-width="2.2"><rect x="3" y="5" width="18" height="14" rx="2"/><path d="M3 7l9 6 9-6"/></svg>
        info@tidewellfellowship.example
      </div>
      <div class="contact-line">
        <svg viewBox="0 0 24 24" fill="none" stroke="currentColor" stroke-width="2.2"><circle cx="12" cy="12" r="9"/><path d="M3 12h18M12 3c3 3 3 15 0 18M12 3c-3 3-3 15 0 18"/></svg>
        www.tidewellfellowship.example
      </div>
    </div>
  </section>
</main>
</body>
</html>
```